Social Media Graphics - Harbor Climb REVISED

Create 6-7 individual social media graphics (square size) to encourage folks to join our online course called:

The Lantern Ledger Plan
How to Launch a Multi-Million Business From Scratch
Sign Up Today!

IMPORTANT: Make the largest and most prominent text on the graphic be: How to Launch a Multi-Million Business From Scratch

For the color scheme of the graphics, let's try a blue color palette; make sure the graphics appeal to both men and women

Make sure each graphic contains 1 of the 3 pics attached (crop pic as needed); and make sure one of the graphics is all TEXT only.

Target Market(s)

men and women looking to start a business

Industry/Entity Type

Entrepreneurship

Colors
0054AA
0677BA
7BADD7
CADEEF
E8F1F8

Requirements
Must have
• All the text and use the 3 pics provided; one graphic can be all text; Simple, modern design that's easy to read

```html
<!DOCTYPE html>
<html lang="en">
<head>
<meta charset="utf-8">
<title>The Lantern Ledger Plan – Social Graphics</title>
<link rel="stylesheet" href="https://fonts.googleapis.com/css2?family=Oswald:wght@500;700&display=swap">
<style>
:root{
  --blue-deep:#0054aa;
  --blue:#0677ba;
  --blue-mid:#7badd7;
  --blue-light:#cadeef;
  --blue-pale:#e8f1f8;
  --white:#ffffff;
  --navy:#0a3f7a;
}
*{margin:0;padding:0;box-sizing:border-box}
html,body{width:1200px;height:622px;overflow:hidden}
body{background:var(--blue-pale);font-family:"Oswald",sans-serif;position:relative}
.tile{position:absolute;width:256px;height:256px;overflow:hidden;box-shadow:0 2px 8px rgba(0,60,120,.15)}
.r1{top:36px}.r2{top:330px}
.c1{left:40px}.c2{left:328px}.c3{left:616px}.c4{left:904px}

.photo{position:absolute}
.photo-office{inset:0;background:linear-gradient(135deg,#3a2a20 0%,#b59a7c 35%,#e9dcc6 55%,#6d5a4a 80%,#2a2a2e 100%)}
.photo-duo{background:linear-gradient(160deg,#2f5f95 0%,#1d2a3f 45%,#121820 100%)}
.photo-duo-red{background:linear-gradient(160deg,#3b2a28 0%,#c23a4a 45%,#1c1c22 100%)}
.photo-duo-blue{background:linear-gradient(160deg,#3a2c26 0%,#2455a8 50%,#1a1a1f 100%)}
.skyline{inset:0;background:linear-gradient(130deg,#1b6fb8 0%,#0c5aa5 40%,#0a4c92 70%,#2c7cc2 100%)}

.brand{position:absolute;display:flex;align-items:center;gap:6px;color:var(--white);font-weight:700;font-size:17px;line-height:1;white-space:nowrap}
.brand-mark{width:24px;height:24px;border:3px solid currentColor;border-radius:3px;flex:none}
.brand.dark{color:var(--blue-deep)}

.cta{position:absolute;font-weight:700;font-size:10px;letter-spacing:.2px;text-align:center;border-radius:4px;padding:3px 0;color:var(--blue-deep);background:var(--blue-light)}
.cta.solid{background:var(--blue-deep);color:var(--white);border:1px solid var(--blue-mid)}
.cta.big{font-size:15px;padding:4px 0;border-radius:8px}

.head{position:absolute;color:var(--white);font-weight:700;line-height:.95;text-transform:uppercase}
.head .sm{font-weight:500;font-size:15px;display:block}
.head .md{font-size:24px;display:block}
.head .lg{font-size:32px;display:block;letter-spacing:-.3px}
.head .ft{font-weight:500;font-size:17px;display:block;margin-top:4px}
.head.lift{text-shadow:0 2px 3px rgba(0,40,90,.45)}
.head.outline{text-shadow:2px 0 0 var(--blue-deep),-2px 0 0 var(--blue-deep),0 2px 0 var(--blue-deep),0 -2px 0 var(--blue-deep),2px 2px 0 var(--blue-deep),-2px -2px 0 var(--blue-deep),2px -2px 0 var(--blue-deep),-2px 2px 0 var(--blue-deep)}
.head.dark{color:var(--blue-deep)}
.band{position:absolute;background:var(--blue-deep)}
</style>
</head>
<body>

<!-- Tile 1 -->
<section class="tile r1 c1" style="background:var(--blue-deep)">
  <div class="photo skyline" role="img" aria-label="Faded office tower with a rising arrow in blue tones"></div>
  <div class="brand" style="left:28px;top:30px"><span class="brand-mark"></span>The Lantern Ledger Plan</div>
  <h2 class="head lift" style="left:28px;top:106px">
    <span class="sm">How to</span><span class="md">Launch a</span><span class="lg">Multi-Million</span><span class="md">Business</span><span class="ft">From Scratch</span>
  </h2>
  <div class="cta" style="left:156px;top:218px;width:76px">SIGN UP TODAY!</div>
</section>

<!-- Tile 2 -->
<section class="tile r1 c2">
  <div class="photo photo-office" role="img" aria-label="Two course hosts presenting on stage in a bright office space"></div>
  <div class="brand" style="left:18px;top:14px;font-size:19px"><span class="brand-mark" style="width:30px;height:30px"></span>The Lantern Ledger Plan</div>
  <h2 class="head outline" style="left:20px;top:106px">
    <span class="sm">How to</span><span class="md">Launch a</span><span class="lg">Multi-Million</span><span class="md">Business</span><span class="ft">From Scratch</span>
  </h2>
  <div class="cta solid" style="left:140px;top:220px;width:102px">SIGN UP TODAY!</div>
</section>

<!-- Tile 3 -->
<section class="tile r1 c3" style="background:linear-gradient(170deg,var(--blue-light) 0%,var(--blue-pale) 45%,var(--blue-light) 100%)">
  <div class="photo photo-duo" style="left:40px;top:60px;width:216px;height:170px;border-radius:60px 60px 0 0" role="img" aria-label="Portrait of the two course hosts smiling, arms crossed"></div>
  <h2 class="head dark" style="left:16px;top:14px">
    <span class="sm" style="font-size:13px">How to <span style="font-size:22px;font-weight:700">Launch a</span></span><span class="lg" style="font-size:36px">Multi-Million</span><span class="md" style="font-size:21px">Business</span><span class="ft" style="font-size:11px;margin-top:2px">From Scratch</span>
  </h2>
  <div class="band" style="left:0;top:192px;width:256px;height:64px"></div>
  <div class="brand" style="left:24px;top:208px"><span class="brand-mark" style="width:30px;height:30px"></span>The Lantern Ledger Plan</div>
  <div class="cta" style="left:172px;top:232px;width:68px;font-size:9px">SIGN UP TODAY!</div>
</section>

<!-- Tile 4 -->
<section class="tile r1 c4" style="background:var(--blue-light)">
  <div class="band" style="left:-20px;top:-40px;width:300px;height:110px;transform:rotate(-8deg)"></div>
  <div class="photo photo-duo" style="left:20px;top:50px;width:236px;height:170px;border-radius:70px 70px 0 0" role="img" aria-label="Portrait of the two course hosts smiling together"></div>
  <div class="brand" style="left:22px;top:20px;font-size:19px"><span class="brand-mark" style="width:30px;height:30px"></span>The Lantern Ledger Plan</div>
  <div class="band" style="left:-20px;top:182px;width:300px;height:110px;transform:rotate(-8deg)"></div>
  <h2 class="head" style="left:18px;top:160px;transform:rotate(-8deg);transform-origin:left top">
    <span class="sm" style="font-size:12px">How to <span style="font-size:20px;font-weight:700">Launch a</span></span><span class="lg">Multi-Million</span><span class="md" style="font-size:20px;padding-left:30px">Business <span style="font-size:12px;font-weight:500">From Scratch</span></span>
  </h2>
  <div class="cta" style="left:170px;top:232px;width:70px">SIGN UP TODAY!</div>
</section>

<!-- Tile 5 -->
<section class="tile r2 c1" style="background:var(--blue-deep)">
  <div class="photo skyline" role="img" aria-label="Faded office tower with a rising arrow in blue tones"></div>
  <div class="brand" style="left:28px;top:28px"><span class="brand-mark"></span>The Lantern Ledger Plan</div>
  <h2 class="head lift" style="left:24px;top:118px;transform:rotate(-8deg);transform-origin:left top">
    <span class="sm">How to</span><span class="md">Launch a</span><span class="lg">Multi-Million</span><span class="md" style="font-size:28px">Business</span><span class="ft">From Scratch</span>
  </h2>
  <div class="cta" style="left:156px;top:226px;width:76px">SIGN UP TODAY!</div>
</section>

<!-- Tile 6 -->
<section class="tile r2 c2">
  <div class="photo photo-office" role="img" aria-label="Two course hosts presenting on stage in a bright office space"></div>
  <div class="brand" style="left:18px;top:12px;font-size:19px"><span class="brand-mark" style="width:30px;height:30px"></span>The Lantern Ledger Plan</div>
  <h2 class="head outline" style="left:14px;top:130px;text-align:center;width:228px">
    <span class="md" style="font-size:27px">How to Launch a</span><span class="lg" style="font-size:38px">Multi-Million</span><span class="md" style="font-size:19px">Business From Scratch</span>
  </h2>
  <div class="cta solid big" style="left:56px;top:222px;width:144px">SIGN UP TODAY!</div>
</section>

<!-- Tile 7 -->
<section class="tile r2 c3" style="background:linear-gradient(160deg,var(--blue-light) 0%,var(--blue-pale) 40%,var(--blue-light) 70%,var(--blue-mid) 100%)">
  <div class="brand dark" style="left:20px;top:18px"><span class="brand-mark" style="width:30px;height:30px"></span>The Lantern Ledger Plan</div>
  <div class="photo photo-duo-red" style="left:30px;top:52px;width:200px;height:204px;border-radius:80px 80px 0 0" role="img" aria-label="Portrait of the two course hosts laughing together"></div>
  <h2 class="head outline" style="left:16px;top:150px;transform:rotate(-8deg);transform-origin:left top">
    <span class="md" style="font-size:26px">How to Launch a</span><span class="lg" style="font-size:36px">Multi-Million</span><span class="md" style="font-size:19px">Business From Scratch</span>
  </h2>
  <div class="cta solid" style="left:140px;top:228px;width:100px">SIGN UP TODAY!</div>
</section>

<!-- Tile 8 -->
<section class="tile r2 c4" style="background:var(--blue-light)">
  <div class="band" style="left:0;top:0;width:256px;height:98px"></div>
  <h2 class="head" style="left:16px;top:12px;color:var(--blue-light)">
    <span class="md" style="font-size:28px">How to Launch a</span><span class="lg" style="font-size:34px;color:var(--white)">Multi-Million</span><span class="md" style="font-size:19px">Business From Scratch</span>
  </h2>
  <div class="photo photo-duo-blue" style="left:28px;top:98px;width:228px;height:158px;border-radius:60px 60px 0 0" role="img" aria-label="Portrait of the two course hosts smiling together"></div>
  <div class="brand" style="left:20px;top:194px;font-size:19px"><span class="brand-mark" style="width:30px;height:30px"></span>The Lantern Ledger Plan</div>
  <div class="cta solid big" style="left:82px;top:222px;width:132px">SIGN UP TODAY!</div>
</section>

</body>
</html>
```